Hey,
My name is Tomas Vellanegra and I'm starting a PhD in Physics next year. I want to a bit more than just research on my own. I want to bring some public involvement to it.
"Zeta Quarks" is website/wordpress/blog. It is a way to bring physics to the general public without losing the math or the physics essence - This is a place to share fun and interesting findings that PhD students, Professors, High school students and basically everyone else that loves and wants to know a bit more about nature. The idea is to put real science to debate in a open non-judgmental way in prol of knowledge and discovery. "Everybody" is welcome to post relevant things such as experiments made at home as well as their latest discovery in their super high tech £100M lab.
The first step of the project is to develop a BLOG (Wordpress) - the domain is already register "zetaquarks.org and zetaquarks.com" that could host that initial debate and posts.
Think http://lensmoravia.org/ ; http://www.wavecellar.org/; https://www.youtube.com/user/ninetyglyphs; https://www.youtube.com/user/secondquanta as a guidelines...
http://trevilo.bvx.com.br/
I would enjoy touches of watercolour design here and there.
I also like pastel colours. But remember, I am a scientist and not at all designer. I'll trust the artists to create and show me what they are up to.
UPDATE: Just so you guys know. I want to do a Website in form of a Blog. I want to easily post and upload videos and articles related to Physics.
I'm more familiar with Wordpress but if you say that any other platform does the job better and I can still maintain the domain zetaquarks.org lets do it!
Update number 2: I will respond every designer asap. I will however do that between 9:00am and 14:00 pm Brasilia/Brazil Time.
So please don't get upset or take it personal if you don't get a feedback right away, specially if it is 02:00 a.m my time, ok ?! : - )
Thanks Guys and good work!
For all designers that just want to do logos please post them in: Manage Project | Zeta Quarks - Logo Design Project
We will continue from there!
Target Market(s)
Everyone that likes physics, no matter if you are a Nobel Laureate or a single mother that likes physics.
Industry/Entity Type
Artists
Font styles to use
Other font styles liked:
- I like Calibri, Helvetica, Verdana, Univers and Tahoma for body text, Sometimes I use Arial. Cambria and Georgia for headings
Requirements
Must have
- I'm open minded! But I like thinks to be simple!
Nice to have
- The way you going to put "Zeta Quarks" is completely up to you. I usually like it simple but. Show me what you got and I'll give you feedback if I like it or not! Just remember to keep it clean and user friendly.
Should not have
- Just try beautiful and functional designs. I usually don't like super old style fonts like Times New Roman and very elaborate things that are hard to read.

```html
<!DOCTYPE html>
<html lang="en">
<head>
<meta charset="utf-8">
<title>Zeta Quarks</title>
<link href="https://fonts.googleapis.com/css2?family=Carlito:wght@400;700&display=swap" rel="stylesheet">
<style>
:root{
  --red:#e0474c;
  --red-soft:#e0595e;
  --teal:#7ccbc4;
  --teal-dark:#2f8f80;
  --blue-link:#4a7fb5;
  --purple:#6b3b8a;
  --sky:#2a9fd6;
  --peach:#fce5d4;
  --grey-bg:#efefef;
  --grey-icon:#a9a9a9;
  --text:#6b6b6b;
  --line:#d8d8d8;
  --card-blue:#8aafd6;
  --footer:#2b2b2b;
  --footer-text:#bdbdbd;
}
*{box-sizing:border-box;margin:0;padding:0}
html,body{width:1200px;height:2347px;overflow:hidden}
body{position:relative;background:#fff;font-family:"Carlito",Calibri,Arial,sans-serif;color:var(--text)}
.abs{position:absolute}

/* header */
.brand{left:99px;top:28px;font-size:56px;color:var(--red);line-height:70px;letter-spacing:.5px}
.social{left:774px;top:45px;display:flex;gap:8px}
.social span{width:34px;height:34px;border-radius:50%;display:block}
.login-toggle{left:993px;top:33px;width:108px;height:56px;background:var(--teal);color:#fff;font-size:20px;display:flex;align-items:center;justify-content:center;gap:8px}

/* nav */
.nav{left:99px;top:118px;width:720px;height:56px;border-top:1px solid #9fb8d4}
.nav ul{list-style:none;display:flex;position:absolute;top:10px;left:0;font-size:15px;color:#7a7a7a}
.nav li{position:absolute;white-space:nowrap}
.nav li.active{color:var(--blue-link)}
.ruler{position:absolute;left:0;top:44px;width:100%;height:10px;border-bottom:1px solid #9fb8d4;
  background:repeating-linear-gradient(90deg,#a9bdd3 0 1px,transparent 1px 6px) bottom/100% 5px no-repeat}

/* hero */
.hero{left:99px;top:194px;width:1002px;height:327px;background:radial-gradient(ellipse at 35% 55%,#2f5a2a 0%,#122012 40%,#050505 75%)}
.hero-caption{left:704px;top:296px;font-size:27px;color:#f2a646;white-space:nowrap}

/* login panel */
.login-panel{left:817px;top:106px;width:284px;height:402px;background:#fff;box-shadow:0 0 6px rgba(0,0,0,.18)}
.login-panel h3{position:absolute;left:12px;top:14px;font-size:23px;color:var(--red);font-weight:400;display:flex;align-items:center;gap:6px}
.field{position:absolute;left:12px;width:260px;height:41px;background:var(--peach);font-size:13px;color:#8a7060;padding:12px 18px}
.btn{position:absolute;display:flex;align-items:center;justify-content:center;font-size:15px}
.btn-login{left:201px;top:157px;width:72px;height:41px;background:var(--red-soft);color:#fff}
.btn-register{left:12px;top:219px;width:260px;height:41px;background:#e0e0e0;color:#555}
.btn-social{left:12px;width:260px;height:52px;color:#fff;font-weight:700;gap:10px;font-size:16px}
.btn-social i{width:26px;height:26px;border-radius:50%;background:#fff;display:block}

/* posts */
.post{left:99px;width:719px;height:261px;border-bottom:1px solid var(--line)}
.post .thumb{position:absolute;left:0;top:0;width:208px;height:194px}
.post h2{position:absolute;left:228px;top:2px;width:480px;font-size:23px;line-height:29px;font-weight:400;color:var(--blue-link)}
.post .meta{position:absolute;left:228px;top:64px;font-size:11px;color:var(--red)}
.post .meta span{margin-left:10px}
.post p{position:absolute;left:228px;top:90px;width:485px;font-size:12.5px;line-height:19.5px;color:#777}
.share{position:absolute;left:235px;top:166px;display:flex;gap:8px}
.share span{width:33px;height:33px;border-radius:50%;background:var(--grey-icon);display:flex;align-items:center;justify-content:center}
.play{position:absolute;left:78px;top:82px}

.author-card{position:absolute;left:0;top:0;width:208px;height:194px;background:var(--card-blue);color:#fff}
.avatar{position:absolute;left:13px;top:24px;width:62px;height:62px;border-radius:50%;border:3px solid #fff;background:linear-gradient(#c98d6c,#8b5a44)}
.author-card .name{position:absolute;left:91px;top:22px;font-size:17px;font-weight:700;color:#f3e36a}
.author-card .role{position:absolute;left:91px;top:49px;font-size:11px;line-height:25px}
.author-card .tax{position:absolute;left:18px;font-size:12px;display:flex;align-items:center;gap:10px}

.pager{left:537px;top:2127px;display:flex;gap:4px}
.pager span{width:22px;height:22px;background:#ddd;border-radius:3px;font-size:9px;color:#fff;display:flex;align-items:center;justify-content:center}
.pager span.current{background:#8a8a8a}
.pager .gap{background:none;color:#aaa;width:12px}

/* sidebar */
.side-title{left:839px;font-size:23px;font-weight:400}
.mini{left:839px;width:262px;height:97px;background:var(--grey-bg)}
.mini .thumb{position:absolute;left:0;top:0;width:97px;height:97px}
.mini p{position:absolute;left:114px;top:8px;width:140px;font-size:12px;line-height:18px;color:#777}
.mini .date{position:absolute;left:114px;top:72px;font-size:11px}
.top .date{color:var(--purple)}
.viewed .date{color:var(--teal-dark)}

.newsletter{left:839px;top:1075px;width:262px;height:41px;display:flex}
.newsletter span:first-child{flex:1;background:var(--peach);font-size:12px;color:#8a7060;padding:13px 16px}
.newsletter span:last-child{width:84px;background:var(--red-soft);color:#fff;font-size:13px;display:flex;align-items:center;justify-content:center}

.feed{left:839px;top:1665px;width:262px;height:310px;border:2px solid #bfe0f0;padding:0 16px}
.tweet{position:absolute;left:16px;width:230px;font-size:11.5px;line-height:18px;color:#333}
.tweet .handle{color:var(--sky);margin-bottom:10px}
.tweet .handle em{font-style:normal;color:#999}
.tweet a{color:var(--sky);text-decoration:none}
.tweet .actions{margin-top:8px;font-size:10px;color:var(--sky);background:#eef6fb;display:flex;gap:10px;padding:0 4px}

/* footer */
.footer{left:0;top:2201px;width:1200px;height:146px;background:var(--footer)}
.footer-links{position:absolute;left:0;top:27px;width:1200px;display:flex;justify-content:center;gap:36px;font-size:14px;color:var(--footer-text)}
.footer-links li{list-style:none}
.footer-links li::before{content:"• ";color:#888}
.footer-rule{position:absolute;left:99px;top:69px;width:1002px;border-top:1px solid #444}
.copyright{position:absolute;left:101px;top:97px;font-size:14px;color:var(--footer-text)}
.footer-icons{position:absolute;left:1016px;top:88px;display:flex;gap:13px}
.footer-icons span{width:34px;height:34px;border-radius:50%;background:#bdbdbd;display:flex;align-items:center;justify-content:center}
</style>
</head>
<body>

<header>
  <div class="abs brand">Zeta Quarks</div>
  <div class="abs social" aria-label="Social links">
    <span style="background:#7b93bf"></span>
    <span style="background:#7cc0de"></span>
    <span style="background:#e08a87"></span>
    <span style="background:#6f6f6f"></span>
    <span style="background:#8fbf7c"></span>
  </div>
  <div class="abs login-toggle">
    <svg width="18" height="22" viewBox="0 0 18 22"><path d="M4 10V6a5 5 0 0 1 10 0v4" fill="none" stroke="#fff" stroke-width="2.4"/><rect x="1" y="10" width="16" height="12" rx="1.5" fill="#fff"/></svg>
    Login
  </div>

  <nav class="abs nav">
    <ul>
      <li class="active" style="left:28px">Home</li>
      <li style="left:137px">About us</li>
      <li style="left:265px">The Autors</li>
      <li style="left:408px">Categories</li>
      <li style="left:548px">Upload article</li>
      <li style="left:710px">FAQ</li>
    </ul>
    <div class="ruler"></div>
  </nav>
</header>

<section class="abs hero" role="img" aria-label="Photo of a researcher in safety goggles aligning green laser beams on an optical table"></section>
<div class="abs hero-caption">Etiam varius lorem</div>

<aside class="abs login-panel">
  <h3>
    <svg width="28" height="18" viewBox="0 0 28 18"><circle cx="8" cy="9" r="6" fill="none" stroke="#e0474c" stroke-width="3"/><path d="M13 9h14M22 9v5M26 9v4" stroke="#e0474c" stroke-width="3"/></svg>
    Login
  </h3>
  <div class="field" style="top:52px">Email ID</div>
  <div class="field" style="top:105px">Username</div>
  <div class="btn btn-login">LOGIN</div>
  <div class="btn btn-register">Register Now</div>
  <div class="btn btn-social" style="top:271px;background:#3d5a98"><i></i>SIGN IN VIA FRIENDLINK</div>
  <div class="btn btn-social" style="top:335px;background:#333"><i></i>SIGN IN VIA POSTBOX</div>
</aside>

<main>
  <article class="abs post" style="top:565px">
    <div class="author-card">
      <div class="avatar" role="img" aria-label="Author portrait"></div>
      <div class="name">Ravi Holmgren</div>
      <div class="role">Aliquam mollis odio<br>Nobel Laureates</div>
      <div class="tax" style="top:124px">
        <svg width="14" height="12" viewBox="0 0 14 12"><path d="M0 0h6l6 6-6 6-6-6z" fill="#fff"/></svg>Tag name</div>
      <div class="tax" style="top:157px">
        <svg width="14" height="12" viewBox="0 0 14 12"><path d="M0 1h3M5 1h9M0 6h3M5 6h9M0 11h3M5 11h9" stroke="#fff" stroke-width="2"/></svg>Category name</div>
    </div>
    <h2>Aenean fringilla neque tristique elit ultricies commodo facilisis</h2>
    <div class="meta">Sep 2, 2014 <span>• 18 Comments</span></div>
    <p>Morbi in mauris odio. Praesent at congue lacus, in volutpat magna. Nulla at augue leo. Interdum et malesuada fames ac ante ipsum primis in faucibus. Sed congue commodo sapien eget.</p>
    <div class="share"><span></span><span></span><span></span><span></span></div>
  </article>

  <article class="abs post" style="top:826px">
    <div class="thumb" role="img" aria-label="Video still of a molecular structure model" style="background:radial-gradient(circle at 50% 55%,#8a6f7a,#5c5c5c 45%,#3a3a3a)"></div>
    <svg class="play" width="52" height="34" viewBox="0 0 52 34"><rect width="52" height="34" rx="6" fill="#111"/><path d="M20 9l14 8-14 8z" fill="#fff"/></svg>
    <h2>Curabitur sollicitudin odio ligula, ultricies porttitor tellus vestibulum</h2>
    <div class="meta">Sep 2, 2014 <span>• 18 Comments</span></div>
    <p>Morbi in mauris odio. Praesent at congue lacus, in volutpat magna. Nulla at augue leo. Interdum et malesuada fames ac ante ipsum primis in faucibus. Sed congue commodo sapien eget.</p>
    <div class="share"><span></span><span></span><span></span><span></span></div>
  </article>

  <article class="abs post" style="top:1087px">
    <div class="thumb" role="img" aria-label="Photo of pressure gauges on laboratory equipment" style="background:linear-gradient(135deg,#6b4a3a,#a88a72 45%,#3a2a22)"></div>
    <h2>Cras iaculis aliquam diam, eu ultrices magna semper etamet</h2>
    <div class="meta">Sep 2, 2014 <span>• 18 Comments</span></div>
    <p>Morbi in mauris odio. Praesent at congue lacus, in volutpat magna. Nulla at augue leo. Interdum et malesuada fames ac ante ipsum primis in faucibus. Sed congue commodo sapien eget.</p>
    <div class="share"><span></span><span></span><span></span><span></span></div>
  </article>

  <article class="abs post" style="top:1348px">
    <div class="thumb" role="img" aria-label="Illustration of glowing particles in deep space" style="background:radial-gradient(circle at 50% 45%,#c46a3a,#3a4a8a 40%,#0a0d1e 75%)"></div>
    <h2>Vivamus facilisis erat ac purus vestibulum, quis luctus turpis iaculis</h2>
    <div class="meta">Sep 2, 2014 <span>• 18 Comments</span></div>
    <p>Morbi in mauris odio. Praesent at congue lacus, in volutpat magna. Nulla at augue leo. Interdum et malesuada fames ac ante ipsum primis in faucibus. Sed congue commodo sapien eget.</p>
    <div class="share"><span></span><span></span><span></span><span></span></div>
  </article>

  <article class="abs post" style="top:1609px">
    <div class="thumb" role="img" aria-label="Video still of a bright light burst" style="background:radial-gradient(circle at 45% 50%,#f6c27a,#b8521c 30%,#120806 70%)"></div>
    <svg class="play" width="52" height="34" viewBox="0 0 52 34"><rect width="52" height="34" rx="6" fill="#111"/><path d="M20 9l14 8-14 8z" fill="#fff"/></svg>
    <h2>Sed sagittis mi sit amet est bibendum, porttitor dictum sapien lobortis</h2>
    <div class="meta">Sep 2, 2014 <span>• 18 Comments</span></div>
    <p>Morbi in mauris odio. Praesent at congue lacus, in volutpat magna. Nulla at augue leo. Interdum et malesuada fames ac ante ipsum primis in faucibus. Sed congue commodo sapien eget.</p>
    <div class="share"><span></span><span></span><span></span><span></span></div>
  </article>

  <article class="abs post" style="top:1870px">
    <div class="thumb" role="img" aria-label="Photo of an airliner on a runway" style="background:linear-gradient(#3a78c0,#8fb8e0 60%,#c89a8a)"></div>
    <h2>Phasellus sit amet felis sed libero iaculis egestas habitant.</h2>
    <div class="meta">Sep 2, 2014 <span>• 18 Comments</span></div>
    <p>Morbi in mauris odio. Praesent at congue lacus, in volutpat magna. Nulla at augue leo. Interdum et malesuada fames ac ante ipsum primis in faucibus. Sed congue commodo sapien eget.</p>
    <div class="share"><span></span><span></span><span></span><span></span></div>
  </article>

  <nav class="abs pager">
    <span class="current">1</span><span>2</span><span>3</span><span>4</span><span>5</span><span>6</span><span>7</span><span>8</span><span>»</span><span class="gap">…</span><span>»»</span>
  </nav>
</main>

<aside>
  <h3 class="abs side-title" style="top:558px;color:var(--purple)">Top Articles</h3>
  <div class="abs mini top" style="top:595px"><div class="thumb" role="img" aria-label="Radio telescope dish at dusk" style="background:linear-gradient(#3a4a8a,#c89a4a)"></div><p>Nam libero justo, tristique nec feugiat in, porta at lorem</p><span class="date">Sep 2, 2014</span></div>
  <div class="abs mini top" style="top:699px"><div class="thumb" role="img" aria-label="Atom model illustration" style="background:radial-gradient(#e8f4f2,#7fb8b0)"></div><p>Nam libero justo, tristique nec feugiat in, porta at lorem</p><span class="date">Sep 2, 2014</span></div>
  <div class="abs mini top" style="top:804px"><div class="thumb" role="img" aria-label="Prism splitting light into a spectrum" style="background:linear-gradient(135deg,#1a2a7a,#8a6ad0 55%,#3a1a6a)"></div><p>Nam libero justo, tristique nec feugiat in, porta at lorem</p><span class="date">Sep 2, 2014</span></div>
  <div class="abs mini top" style="top:907px"><div class="thumb" role="img" aria-label="Plasma globe glowing" style="background:radial-gradient(circle at 50% 60%,#f0a0c0,#a02a6a 30%,#120612 70%)"></div><p>Nam libero justo, tristique nec feugiat in, porta at lorem</p><span class="date">Sep 2, 2014</span></div>

  <h3 class="abs side-title" style="top:1040px;color:var(--red);display:flex;align-items:center;gap:8px">
    <svg width="28" height="20" viewBox="0 0 28 20"><rect x="1" y="1" width="26" height="18" fill="none" stroke="#e0474c" stroke-width="2.4"/><path d="M1 1l13 10L27 1" fill="none" stroke="#e0474c" stroke-width="2.4"/></svg>
    Newsletter Signup</h3>
  <div class="abs newsletter"><span>Email ID</span><span>Subscribe</span></div>

  <h3 class="abs side-title" style="top:1145px;color:var(--teal-dark)">Most Viewed</h3>
  <div class="abs mini viewed" style="top:1181px"><div class="thumb" role="img" aria-label="Abstract light rings" style="background:radial-gradient(#8ab0c8,#1a2a3a 70%)"></div><p>Nam libero justo, tristique nec feugiat in, porta at lorem</p><span class="date">Sep 2, 2014</span></div>
  <div class="abs mini viewed" style="top:1286px"><div class="thumb" role="img" aria-label="Hand holding a paper sheet" style="background:linear-gradient(#d8c8b8,#a87a5a)"></div><p>Nam libero justo, tristique nec feugiat in, porta at lorem</p><span class="date">Sep 2, 2014</span></div>
  <div class="abs mini viewed" style="top:1391px"><div class="thumb" role="img" aria-label="Solar panel on green grass" style="background:linear-gradient(#8ac0e8,#6ab04a 60%)"></div><p>Nam libero justo, tristique nec feugiat in, porta at lorem</p><span class="date">Sep 2, 2014</span></div>
  <div class="abs mini viewed" style="top:1496px"><div class="thumb" role="img" aria-label="Glowing energy field over a device" style="background:radial-gradient(circle at 50% 40%,#f0d060,#3a5a7a 40%,#0a1420 75%)"></div><p>Nam libero justo, tristique nec feugiat in, porta at lorem</p><span class="date">Sep 2, 2014</span></div>

  <h3 class="abs side-title" style="top:1632px;color:var(--sky)">Chirper Feed</h3>
  <div class="abs feed">
    <div class="tweet" style="top:14px">
      <div class="handle">Ravi Holmgren <em>@zetaquarks</em></div>
      Nulla tincidunt elit a mauris pulvinar molestie. <a>Nulla suscipit lacus arcu</a>, ac rutrum tellus feugiat sit amet.
      <div class="actions"><span>↩ Reply</span><span>⇄ Retweet</span><span>★ Favorite</span><span>••• More</span></div>
    </div>
    <div class="tweet" style="top:160px">
      <div class="handle">Ravi Holmgren <em>@zetaquarks</em></div>
      Nulla tincidunt elit a mauris pulvinar molestie. <a>Nulla suscipit lacus arcu</a>, ac rutrum tellus feugiat sit amet.
      <div class="actions"><span>↩ Reply</span><span>⇄ Retweet</span><span>★ Favorite</span><span>••• More</span></div>
    </div>
  </div>
</aside>

<footer class="abs footer">
  <ul class="footer-links">
    <li>Home</li><li>About us</li><li>Categories</li><li>FAQ</li><li>Students</li><li>Professors</li><li>Upload Article</li><li>Register</li><li>Login</li>
  </ul>
  <div class="footer-rule"></div>
  <div class="copyright">Copyright © 2014 Zeta Quarks. &nbsp;All rights reserved.</div>
  <div class="footer-icons">
    <span><svg width="18" height="13" viewBox="0 0 18 13"><rect width="18" height="13" fill="#2b2b2b"/><path d="M0 0l9 7 9-7" fill="none" stroke="#bdbdbd" stroke-width="1.6"/></svg></span>
    <span><svg width="18" height="12" viewBox="0 0 18 12"><path d="M2 10l7-7 7 7" fill="none" stroke="#2b2b2b" stroke-width="3.5"/></svg></span>
  </div>
</footer>

</body>
</html>
```